PHD-project

i need the figures to be in the same stile. info is inside the file. There are 5 figures that need redesign. this is for PhD.

Target Market(s)

it will be used in my phd

Colors

Designer to choose colors to be used in the design.

```html
<!DOCTYPE html>
<html lang="en">
<head>
<meta charset="utf-8">
<title>PhD Research Figures</title>
<link rel="stylesheet" href="https://fonts.googleapis.com/css2?family=Oswald:wght@400;500&family=Roboto+Condensed:wght@400;700&display=swap">
<style>
  :root {
    --page: #fafafa;
    --panel: #e6e6e6;
    --title: #6b6b6b;
    --ink: #2b2b2b;
    --green: #27a95a;
    --blue: #3593d8;
    --red: #e74b3c;
    --orange: #f39c12;
    --teal: #1cbb99;
    --lime: #92cf5b;
    --line: #8a8a8a;
    --bar: #4a4a4a;
  }
  html, body { margin: 0; padding: 0; width: 1200px; height: 1200px; overflow: hidden; background: var(--page); }
  .canvas { display: block; width: 1200px; height: 1200px; }
  .fig-title { font-family: "Oswald", sans-serif; font-weight: 500; font-size: 56px; fill: var(--title); text-anchor: middle; letter-spacing: 1px; }
  .label { font-family: "Roboto Condensed", sans-serif; fill: #fff; text-anchor: middle; filter: drop-shadow(1px 1px 1px rgba(0,0,0,.35)); }
  .label.label-left { text-anchor: start; }
  .label-lg { font-size: 30px; }
  .label-md { font-size: 26px; }
  .label-sm { font-size: 21px; }
  .label-xs { font-size: 18px; }
  .label-year-range { font-size: 22px; }
  .axis-text { font-family: "Roboto Condensed", sans-serif; font-size: 21px; fill: var(--ink); }
  .note { font-family: "Roboto Condensed", sans-serif; font-size: 18px; fill: var(--ink); text-anchor: middle; }
  .col-head { font-family: "Roboto Condensed", sans-serif; font-weight: 700; font-size: 33px; fill: var(--ink); text-anchor: middle; }
  .rtd { font-family: "Roboto Condensed", sans-serif; font-weight: 700; font-size: 52px; fill: var(--ink); text-anchor: middle; }
  .dim { font-family: "Roboto Condensed", sans-serif; font-size: 23px; fill: var(--ink); text-anchor: middle; }
  .flow { stroke: #555; stroke-width: 2; fill: none; }
</style>
</head>
<body>
<svg class="canvas" viewBox="0 0 1932 1932" xmlns="http://www.w3.org/2000/svg">
  <defs>
    <linearGradient id="mixGreenBlue" x1="0" x2="1"><stop offset="0" stop-color="#27a95a"/><stop offset="1" stop-color="#3593d8"/></linearGradient>
    <linearGradient id="mixOrangeRed" x1="0" x2="1"><stop offset="0" stop-color="#f39c12"/><stop offset="1" stop-color="#e74b3c"/></linearGradient>
    <linearGradient id="cardBody" x1="0" x2="1"><stop offset="0" stop-color="#d9d9d9"/><stop offset=".12" stop-color="#eef0f2"/><stop offset=".85" stop-color="#f4f4f4"/><stop offset="1" stop-color="#c8c8c8"/></linearGradient>
    <linearGradient id="practiceFill" x1="0" y1="0" x2="0" y2="1"><stop offset="0" stop-color="#c9a36a"/><stop offset=".6" stop-color="#b6b9bd"/><stop offset="1" stop-color="#9db8d0"/></linearGradient>
    <linearGradient id="gapFill" x1="0" y1="0" x2="0" y2="1"><stop offset="0" stop-color="#e9b978"/><stop offset="1" stop-color="#a9c3db"/></linearGradient>
    <linearGradient id="theoryFill" x1="0" y1="0" x2="0" y2="1"><stop offset="0" stop-color="#2f7fc4"/><stop offset="1" stop-color="#7fb9e6"/></linearGradient>
    <clipPath id="domeCut"><rect x="0" y="0" width="600" height="372"/></clipPath>
    <clipPath id="greenDome"><circle cx="213" cy="322" r="150"/></clipPath>
    <clipPath id="orangeOval"><ellipse cx="854" cy="289" rx="178" ry="108"/></clipPath>
    <marker id="head" viewBox="0 0 10 10" refX="9" refY="5" markerWidth="8" markerHeight="8" orient="auto-start-reverse"><path d="M0 0 L10 5 L0 10 z" fill="#555"/></marker>
  </defs>

  <!-- Top row titles and panels -->
  <text class="fig-title" x="300" y="100">FIGURE 1</text>
  <text class="fig-title" x="972" y="100">FIGURE 2</text>
  <text class="fig-title" x="1575" y="100">FIGURE 3</text>
  <rect x="0" y="131" width="591" height="326" fill="var(--panel)"/>
  <rect x="636" y="131" width="686" height="326" fill="var(--panel)"/>
  <rect x="1349" y="131" width="583" height="326" fill="var(--panel)"/>

  <!-- Figure 1 -->
  <g class="fig-thinking">
    <g clip-path="url(#domeCut)">
      <circle cx="213" cy="322" r="150" fill="var(--green)"/>
      <circle cx="387" cy="315" r="143" fill="var(--blue)"/>
      <g clip-path="url(#greenDome)"><circle cx="387" cy="315" r="143" fill="url(#mixGreenBlue)"/></g>
    </g>
    <rect x="82" y="370" width="429" height="8" fill="var(--bar)"/>
    <text class="label label-lg" x="142" y="282">Analytic</text>
    <text class="label label-lg" x="142" y="311">Thinking</text>
    <text class="label label-md" x="296" y="296">Design</text>
    <text class="label label-md" x="296" y="325">Thinking</text>
    <text class="label label-lg" x="435" y="276">Intuitive</text>
    <text class="label label-lg" x="435" y="305">and Creative</text>
    <text class="label label-lg" x="435" y="334">Thinking</text>
    <text class="axis-text" x="82" y="405">Understand Problem</text>
    <line x1="270" y1="398" x2="338" y2="398" stroke="#333" stroke-width="2" marker-start="url(#head)" marker-end="url(#head)"/>
    <text class="axis-text" x="354" y="405">Design Solution</text>
  </g>

  <!-- Figure 2 -->
  <g class="fig-contribution">
    <ellipse cx="854" cy="289" rx="178" ry="108" fill="var(--orange)" stroke="#d98a0c" stroke-width="2"/>
    <ellipse cx="1095" cy="289" rx="177" ry="108" fill="var(--red)" stroke="#c9402f" stroke-width="2"/>
    <g clip-path="url(#orangeOval)"><ellipse cx="1095" cy="289" rx="177" ry="108" fill="url(#mixOrangeRed)"/></g>
    <text class="label label-md" x="802" y="265">Design thinking</text>
    <text class="label label-md" x="802" y="291">in management &amp;</text>
    <text class="label label-md" x="802" y="317">business strategy</text>
    <text class="label label-sm" x="975" y="291">Contribution</text>
    <text class="label label-sm" x="975" y="313">Area</text>
    <text class="label label-md" x="1146" y="284">Research through</text>
    <text class="label label-md" x="1146" y="310">design - RTD</text>
  </g>

  <!-- Figure 3 -->
  <g class="fig-reflection">
    <ellipse cx="1517" cy="293" rx="117" ry="147" fill="var(--teal)" stroke="#16a085" stroke-width="2"/>
    <ellipse cx="1660" cy="207" rx="112" ry="32" fill="var(--lime)" fill-opacity=".85" stroke="#7fbf4a" stroke-width="2"/>
    <ellipse cx="1660" cy="374" rx="112" ry="32" fill="var(--lime)" fill-opacity=".85" stroke="#7fbf4a" stroke-width="2"/>
    <text class="label label-sm" x="1495" y="206">Reflection</text>
    <text class="label label-sm" x="1495" y="229">involves</text>
    <text class="label label-sm" x="1495" y="253">three elements</text>
    <text class="label label-xs label-left" x="1418" y="280">• Returning to experience</text>
    <text class="label label-xs label-left" x="1418" y="307">• Attending to feelings</text>
    <text class="label label-xs label-left" x="1418" y="334">• Evaluating experience</text>
    <text class="label label-xs" x="1659" y="214">Reflecting on action</text>
    <text class="label label-xs" x="1659" y="380">Reflecting in action</text>
    <text class="note" x="1775" y="265">Reflection is an active process of</text>
    <text class="note" x="1775" y="285">witnessing one’s own experience in</text>
    <text class="note" x="1775" y="305">order to examine it more closely, gice</text>
    <text class="note" x="1775" y="325">meaning to it, and learn from it</text>
  </g>

  <!-- Figure 4 -->
  <text class="fig-title" x="972" y="549">FIGURE 4</text>
  <rect x="0" y="569" width="1932" height="517" fill="var(--panel)"/>
  <g class="fig-timeline">
    <line x1="148" y1="928" x2="1795" y2="934" stroke="var(--line)" stroke-width="7"/>

    <g class="milestone">
      <line x1="241" y1="872" x2="241" y2="990" stroke="#555" stroke-width="2"/>
      <rect x="149" y="708" width="188" height="150" fill="url(#cardBody)"/>
      <g role="img" aria-label="Innovation network icon"><rect x="186" y="738" width="112" height="100" rx="12" fill="var(--green)" fill-opacity=".28"/></g>
      <rect x="149" y="603" width="188" height="106" fill="var(--green)"/>
      <polygon points="219,708 263,708 241,731" fill="var(--green)"/>
      <rect x="149" y="856" width="188" height="16" fill="var(--green)"/>
      <text class="label label-md" x="243" y="640">Prequel with</text>
      <text class="label label-md" x="243" y="666">student-led</text>
      <text class="label label-md" x="243" y="692">Innovation</text>
      <circle cx="241" cy="928" r="13" fill="var(--green)" stroke="#fff" stroke-width="4"/>
      <ellipse cx="241" cy="1007" rx="70" ry="48" fill="#fff" stroke="#ddd"/>
      <ellipse cx="241" cy="1007" rx="56" ry="38" fill="var(--green)"/>
      <text class="label label-md" x="241" y="1016">2012</text>
    </g>

    <g class="milestone">
      <line x1="608" y1="872" x2="608" y2="990" stroke="#555" stroke-width="2"/>
      <rect x="515" y="710" width="188" height="148" fill="url(#cardBody)"/>
      <g role="img" aria-label="Interview pictogram"><rect x="552" y="740" width="112" height="100" rx="12" fill="var(--red)" fill-opacity=".28"/></g>
      <rect x="515" y="605" width="188" height="106" fill="var(--red)"/>
      <polygon points="586,710 630,710 608,733" fill="var(--red)"/>
      <rect x="515" y="857" width="188" height="16" fill="var(--red)"/>
      <text class="label label-md" x="609" y="654">First round</text>
      <text class="label label-md" x="609" y="680">of interviews</text>
      <circle cx="608" cy="930" r="13" fill="var(--red)" stroke="#fff" stroke-width="4"/>
      <ellipse cx="607" cy="1009" rx="70" ry="48" fill="#fff" stroke="#ddd"/>
      <ellipse cx="607" cy="1009" rx="56" ry="38" fill="var(--red)"/>
      <text class="label label-md" x="607" y="1018">2012</text>
    </g>

    <g class="milestone">
      <line x1="971" y1="874" x2="971" y2="992" stroke="#555" stroke-width="2"/>
      <rect x="878" y="712" width="188" height="148" fill="url(#cardBody)"/>
      <g role="img" aria-label="Speaker pictogram"><rect x="915" y="742" width="112" height="100" rx="12" fill="var(--orange)" fill-opacity=".28"/></g>
      <rect x="878" y="607" width="188" height="106" fill="var(--orange)"/>
      <polygon points="949,712 993,712 971,735" fill="var(--orange)"/>
      <rect x="878" y="859" width="188" height="16" fill="var(--orange)"/>
      <text class="label label-md" x="972" y="669">Interventions</text>
      <circle cx="971" cy="932" r="13" fill="var(--orange)" stroke="#fff" stroke-width="4"/>
      <ellipse cx="970" cy="1011" rx="70" ry="48" fill="#fff" stroke="#ddd"/>
      <ellipse cx="970" cy="1011" rx="56" ry="38" fill="var(--orange)"/>
      <text class="label label-year-range" x="970" y="1019">2013-2015</text>
    </g>

    <g class="milestone">
      <line x1="1337" y1="876" x2="1337" y2="994" stroke="#555" stroke-width="2"/>
      <rect x="1244" y="714" width="188" height="148" fill="url(#cardBody)"/>
      <g role="img" aria-label="Group interview pictogram"><rect x="1281" y="744" width="112" height="100" rx="12" fill="var(--blue)" fill-opacity=".28"/></g>
      <rect x="1244" y="609" width="188" height="106" fill="var(--blue)"/>
      <polygon points="1315,714 1359,714 1337,737" fill="var(--blue)"/>
      <rect x="1244" y="861" width="188" height="16" fill="var(--blue)"/>
      <text class="label label-md" x="1338" y="658">Second round of</text>
      <text class="label label-md" x="1338" y="684">Interviews</text>
      <circle cx="1337" cy="934" r="13" fill="var(--blue)" stroke="#fff" stroke-width="4"/>
      <ellipse cx="1337" cy="1012" rx="70" ry="48" fill="#fff" stroke="#ddd"/>
      <ellipse cx="1337" cy="1012" rx="56" ry="38" fill="var(--blue)"/>
      <text class="label label-md" x="1337" y="1021">2015</text>
    </g>

    <g class="milestone">
      <line x1="1701" y1="878" x2="1701" y2="996" stroke="#555" stroke-width="2"/>
      <rect x="1608" y="716" width="188" height="148" fill="url(#cardBody)"/>
      <g role="img" aria-label="Conversation pictogram"><rect x="1645" y="746" width="112" height="100" rx="12" fill="var(--teal)" fill-opacity=".28"/></g>
      <rect x="1608" y="611" width="188" height="106" fill="var(--teal)"/>
      <polygon points="1679,716 1723,716 1701,739" fill="var(--teal)"/>
      <rect x="1608" y="863" width="188" height="16" fill="var(--teal)"/>
      <text class="label label-md" x="1702" y="647">Additional</text>
      <text class="label label-md" x="1702" y="673">interviews and</text>
      <text class="label label-md" x="1702" y="699">comments</text>
      <circle cx="1701" cy="935" r="13" fill="var(--teal)" stroke="#fff" stroke-width="4"/>
      <ellipse cx="1700" cy="1013" rx="70" ry="48" fill="#fff" stroke="#ddd"/>
      <ellipse cx="1700" cy="1013" rx="56" ry="38" fill="var(--teal)"/>
      <text class="label label-md" x="1700" y="1022">2017</text>
    </g>
  </g>

  <!-- Figure 5 -->
  <text class="fig-title" x="972" y="1182">FIGURE 5</text>
  <rect x="0" y="1221" width="1932" height="649" fill="var(--panel)"/>
  <g class="fig-framework">
    <text class="col-head" x="291" y="1297">POSITIONING THE RESEARCH</text>
    <text class="col-head" x="694" y="1299">RESEARCH APPROACH</text>
    <text class="col-head" x="1132" y="1301">METHODS</text>
    <text class="col-head" x="1441" y="1302">FINDINGS</text>
    <text class="col-head" x="1741" y="1303">CONTRIBUTION</text>

    <g class="positioning">
      <ellipse cx="296" cy="1430" rx="67" ry="112" fill="var(--orange)" stroke="#d98a0c" stroke-width="2"/>
      <ellipse cx="294" cy="1670" rx="84" ry="172" fill="var(--blue)" stroke="#2a7fc0" stroke-width="2"/>
      <ellipse cx="294" cy="1610" rx="65" ry="115" fill="url(#theoryFill)"/>
      <ellipse cx="295" cy="1450" rx="50" ry="62" fill="url(#practiceFill)"/>
      <ellipse cx="295" cy="1508" rx="48" ry="32" fill="url(#gapFill)"/>
      <text class="label label-sm" x="296" y="1356">Design</text>
      <text class="label label-sm" x="296" y="1379">thinking</text>
      <text class="label label-sm" x="295" y="1439">Design</text>
      <text class="label label-sm" x="295" y="1462">practice</text>
      <text class="label label-sm" x="295" y="1515">Gap</text>
      <text class="label label-sm" x="294" y="1580">Theoretical</text>
      <text class="label label-sm" x="294" y="1604">approach to</text>
      <text class="label label-sm" x="294" y="1628">building design</text>
      <text class="label label-sm" x="294" y="1652">thinking</text>
      <text class="label label-sm" x="294" y="1676">capability</text>
      <text class="label label-sm" x="294" y="1749">Design</text>
      <text class="label label-sm" x="294" y="1771">thinking in</text>
      <text class="label label-sm" x="294" y="1793">organization</text>
    </g>

    <g class="approach">
      <text class="rtd" x="680" y="1368">RtD</text>
      <text class="dim" x="679" y="1413">Learning dimension</text>
      <text class="dim" x="681" y="1440">Pragmatic dimension</text>
      <line x1="476" y1="1455" x2="884" y2="1455" stroke="#333" stroke-width="4" marker-start="url(#head)" marker-end="url(#head)"/>
      <polygon points="463,1470 680,1470 571,1583" fill="var(--orange)"/>
      <polygon points="680,1470 898,1470 789,1583" fill="var(--red)"/>
      <polygon points="680,1470 571,1583 789,1583" fill="#fff"/>
      <polygon points="571,1583 789,1583 680,1695" fill="var(--green)"/>
      <text class="label label-sm" x="567" y="1500">Design</text>
      <text class="label label-sm" x="567" y="1523">practice</text>
      <text class="label label-sm" x="787" y="1501">Design</text>
      <text class="label label-sm" x="787" y="1524">studies</text>
      <text class="label label-sm" x="680" y="1611">Design</text>
      <text class="label label-sm" x="680" y="1634">exploration</text>
    </g>

    <path d="M960 1316 Q985 1316 985 1345 L985 1540 Q985 1567 1013 1567 Q985 1567 985 1595 L985 1792 Q985 1820 960 1820" fill="none" stroke="#666" stroke-width="2"/>

    <rect x="1049" y="1320" width="170" height="505" rx="6" fill="var(--blue)"/>
    <rect x="1355" y="1321" width="169" height="506" rx="6" fill="var(--teal)"/>
    <rect x="1662" y="1323" width="168" height="505" rx="6" fill="var(--lime)"/>

    <g class="methods">
      <text class="label label-sm" x="1134" y="1352">Interventions</text>
      <text class="label label-sm" x="1134" y="1378">design</text>
      <text class="label label-sm" x="1134" y="1422">Reflection on</text>
      <text class="label label-sm" x="1134" y="1448">action</text>
      <text class="label label-sm" x="1134" y="1508">Reflective</text>
      <text class="label label-sm" x="1134" y="1534">conversation with</text>
      <text class="label label-sm" x="1134" y="1559">the situation</text>
      <text class="label label-sm" x="1134" y="1585">(reflection in action)</text>
      <text class="label label-sm" x="1134" y="1648">Proto-practices</text>
      <text class="label label-sm" x="1134" y="1727">Interviews</text>
      <text class="label label-sm" x="1134" y="1797">Observations</text>
    </g>
    <g class="findings">
      <text class="label label-sm" x="1441" y="1358">The value of</text>
      <text class="label label-sm" x="1441" y="1384">semi-structured</text>
      <text class="label label-sm" x="1441" y="1410">tools for</text>
      <text class="label label-sm" x="1441" y="1436">non-designers</text>
      <text class="label label-sm" x="1441" y="1490">Openness as a</text>
      <text class="label label-sm" x="1441" y="1516">type of mindset</text>
      <text class="label label-sm" x="1441" y="1542">supporting</text>
      <text class="label label-sm" x="1441" y="1567">competence</text>
      <text class="label label-sm" x="1441" y="1593">building</text>
      <text class="label label-sm" x="1441" y="1646">The importance</text>
      <text class="label label-sm" x="1441" y="1671">of insiders/</text>
      <text class="label label-sm" x="1441" y="1697">experts</text>
      <text class="label label-sm" x="1441" y="1748">The role of time</text>
      <text class="label label-sm" x="1441" y="1774">during and between</text>
      <text class="label label-sm" x="1441" y="1799">design activities</text>
    </g>
    <g class="contributions">
      <text class="label label-sm" x="1746" y="1361">Semi-structured</text>
      <text class="label label-sm" x="1746" y="1387">and visual</text>
      <text class="label label-sm" x="1746" y="1413">design tools</text>
      <text class="label label-sm" x="1746" y="1439">(paper 1-4)</text>
      <text class="label label-sm" x="1746" y="1500">Framework of 3</text>
      <text class="label label-sm" x="1746" y="1526">core concepts -</text>
      <text class="label label-sm" x="1746" y="1552">dialogue space</text>
      <text class="label label-sm" x="1746" y="1578">(paper 6)</text>
      <text class="label label-sm" x="1746" y="1604">temporabilty</text>
      <text class="label label-sm" x="1746" y="1630">(paper 6)</text>
      <text class="label label-sm" x="1746" y="1656">openness</text>
      <text class="label label-sm" x="1746" y="1681">(paper 6)</text>
      <text class="label label-sm" x="1746" y="1737">Guidelines</text>
      <text class="label label-sm" x="1746" y="1763">(paper 7)</text>
    </g>

    <g class="flows">
      <line class="flow" x1="1221" y1="1357" x2="1349" y2="1383" marker-end="url(#head)"/>
      <line class="flow" x1="1221" y1="1428" x2="1349" y2="1393" marker-end="url(#head)"/>
      <line class="flow" x1="1221" y1="1448" x2="1349" y2="1520" marker-end="url(#head)"/>
      <line class="flow" x1="1221" y1="1460" x2="1349" y2="1645" marker-end="url(#head)"/>
      <line class="flow" x1="1221" y1="1520" x2="1349" y2="1400" marker-end="url(#head)"/>
      <line class="flow" x1="1221" y1="1480" x2="1349" y2="1762" marker-end="url(#head)"/>
      <line class="flow" x1="1221" y1="1632" x2="1349" y2="1408" marker-end="url(#head)"/>
      <line class="flow" x1="1221" y1="1700" x2="1349" y2="1532" marker-end="url(#head)"/>
      <line class="flow" x1="1221" y1="1725" x2="1349" y2="1652" marker-end="url(#head)"/>
      <line class="flow" x1="1221" y1="1790" x2="1349" y2="1778" marker-end="url(#head)"/>
      <line class="flow" x1="1527" y1="1370" x2="1656" y2="1385" marker-end="url(#head)"/>
      <line class="flow" x1="1527" y1="1545" x2="1656" y2="1398" marker-end="url(#head)"/>
      <line class="flow" x1="1527" y1="1560" x2="1656" y2="1564" marker-end="url(#head)"/>
      <line class="flow" x1="1527" y1="1670" x2="1656" y2="1740" marker-end="url(#head)"/>
      <line class="flow" x1="1527" y1="1752" x2="1656" y2="1580" marker-end="url(#head)"/>
      <line class="flow" x1="1527" y1="1765" x2="1656" y2="1750" marker-end="url(#head)"/>
    </g>
  </g>
</svg>
</body>
</html>
```